Birchford Realty Business Card

Business Card:

Somewhere on front of card, please include Broker License Number: 5839162

Website is BirchfordRealty.example

Address is:
7218 Crestover Ave E
Saginaw, MI 48271

I'll let you use creative freedom on the rest; we obviously need Name, Title, Email (@BirchfordRealty.example), Office Phone, Cell Phone.

Don't want any special die-cutting, just a standard size business card.

On the back, include a place for the date and time of an appointment to be written in pen.

Requirements
Must have
• Our logo, attached to email.

```html
<!DOCTYPE html>
<html lang="en">
<head>
<meta charset="utf-8">
<title>Birchford Realty Business Card</title>
<link rel="stylesheet" href="https://fonts.googleapis.com/css2?family=Open+Sans:ital,wght@0,400;0,600;0,700;1,400&display=swap">
<style>
  :root {
    --navy: #2d2b72;
    --grey: #b9babd;
    --white: #ffffff;
    --paper: #fdfdfd;
    --rule: #a9aaae;
    --page: #eeeeec;
  }
  * { margin: 0; padding: 0; box-sizing: border-box; }
  html, body {
    width: 1200px; height: 960px; overflow: hidden;
    background: var(--page);
    font-family: "Open Sans", Arial, sans-serif;
  }
  .card {
    position: absolute; left: 250px; width: 700px; height: 400px;
    overflow: hidden; box-shadow: 0 4px 14px rgba(0,0,0,.18);
  }
  .card-front { top: 50px; background: var(--navy); color: var(--white); }
  .card-back { top: 510px; background: var(--paper); color: var(--navy); }

  /* Front */
  .brand-name {
    position: absolute; left: 38px; top: 96px;
    font-size: 34px; font-weight: 700; color: var(--white); letter-spacing: -0.5px;
    white-space: nowrap;
  }
  .brand-rule {
    position: absolute; left: 38px; top: 148px; width: 200px; height: 2px; background: var(--grey);
  }
  .person { position: absolute; left: 400px; top: 112px; text-align: center; white-space: nowrap; }
  .person-name { font-size: 30px; font-weight: 400; letter-spacing: .5px; color: var(--white); line-height: 1.2; }
  .person-name strong { font-weight: 700; color: var(--grey); }
  .person-title { font-size: 15px; font-style: italic; margin-left: 80px; }

  .contact { position: absolute; left: 40px; font-size: 16px; display: flex; align-items: flex-start; gap: 12px; line-height: 1.3; white-space: nowrap; }
  .contact svg { flex: none; margin-top: 3px; }
  .contact-web { top: 200px; left: 68px; }
  .contact-email { top: 236px; }
  .contact-address { top: 268px; }

  .band-grey { position: absolute; background: var(--grey); }
  .band-bottom { left: 0; right: 0; bottom: 0; height: 56px; }
  .band-step { left: 340px; right: 0; top: 292px; bottom: 0; }
  .houses-front { position: absolute; right: 14px; top: 236px; width: 120px; height: 56px; background: var(--grey); }

  .license { position: absolute; left: 350px; top: 272px; font-size: 10px; color: var(--white); white-space: nowrap; }
  .phone { position: absolute; display: flex; align-items: center; gap: 10px; font-size: 17px; color: var(--navy); white-space: nowrap; }
  .phone-office { left: 38px; bottom: 16px; }
  .phone-cell { left: 370px; top: 304px; }

  /* Back */
  .back-brand {
    position: absolute; right: 60px; top: 30px;
    font-size: 30px; font-weight: 700; color: var(--navy); letter-spacing: -0.3px;
  }
  .write-line { position: absolute; left: 40px; right: 40px; height: 2px; background: var(--rule); }
  .line-date { top: 150px; }
  .line-time { top: 222px; }
  .write-label { position: absolute; left: 0; right: 0; text-align: center; font-size: 17px; font-style: italic; color: var(--navy); }
  .label-date { top: 158px; }
  .label-time { top: 230px; }
  .band-navy { position: absolute; left: 0; right: 0; bottom: 0; height: 96px; background: var(--navy); }
  .houses-back { position: absolute; right: 60px; bottom: 90px; width: 110px; height: 60px; background: var(--navy); }
</style>
</head>
<body>

<section class="card card-front" aria-label="Card front">
  <div class="brand-name">Birchford Realty</div>
  <div class="brand-rule"></div>

  <div class="person">
    <div class="person-name">JOHN <strong>DOE</strong></div>
    <div class="person-title">Title</div>
  </div>

  <div class="contact contact-web">BirchfordRealty.example</div>
  <div class="contact contact-email">
    <svg width="16" height="12" viewBox="0 0 16 12" aria-hidden="true"><rect x="0.5" y="0.5" width="15" height="11" fill="#fff"/><path d="M1 1l7 6 7-6" fill="none" stroke="#2d2b72" stroke-width="1.4"/></svg>
    <span>john@BirchfordRealty.example</span>
  </div>
  <div class="contact contact-address">
    <svg width="16" height="16" viewBox="0 0 16 16" aria-hidden="true"><path d="M8 1C5 1 3 3.2 3 6c0 3.6 5 9 5 9s5-5.4 5-9c0-2.8-2-5-5-5z" fill="#fff"/><circle cx="8" cy="6" r="1.8" fill="#2d2b72"/></svg>
    <span>7218 Crestover Ave E<br>Saginaw, MI 48271</span>
  </div>

  <div class="band-grey band-step"></div>
  <div class="band-grey band-bottom"></div>
  <div class="houses-front" role="img" aria-label="Silhouette of two houses"></div>

  <div class="license">Broker License Number: 5839162</div>

  <div class="phone phone-cell">
    <svg width="12" height="18" viewBox="0 0 12 18" aria-hidden="true"><rect x="1" y="1" width="10" height="16" rx="2" fill="#2d2b72"/><rect x="3" y="3.5" width="6" height="8" fill="#b9babd"/><circle cx="6" cy="14.3" r="1.1" fill="#b9babd"/></svg>
    <span>+18 1234 1234 1234</span>
  </div>
  <div class="phone phone-office">
    <svg width="16" height="16" viewBox="0 0 16 16" aria-hidden="true"><path d="M3.5 1.5l2.5 3-1.5 1.8c.9 2 2.4 3.5 4.3 4.3L10.6 9l3 2.5-1.4 2.6C7 13.6 2.4 9 1.9 3z" fill="#2d2b72"/></svg>
    <span>+18 1234 1234 1234</span>
  </div>
</section>

<section class="card card-back" aria-label="Card back">
  <div class="back-brand">Birchford Realty</div>

  <div class="write-line line-date"></div>
  <div class="write-label label-date">Date</div>
  <div class="write-line line-time"></div>
  <div class="write-label label-time">Time</div>

  <div class="houses-back" role="img" aria-label="Silhouette of two houses"></div>
  <div class="band-navy"></div>
</section>

</body>
</html>
```